Business card design for Virtual Assistance company

I need a business card designed for my virtual assistance company. We are a small company who services primarily C-level executive clients. The card needs to be double sided with the following contact information on the back:
Melanie Hartwick
Owner/CEO
info@pbtadvisory.net
www.pbtadvisory.net
240.395.2817

The front side should just have the company name incorporated: "PBT Advisory" and "virtual assistance"

The card should be simplistic, but eye catching and should speak to high level executives. Our primary focus areas consist of executive assistance and government contracting.

Target Market(s)

CEOs and executives

Contact Information for Business Card

see project description. phone, email, website.

Colors

Designer to choose only greyscale colors for use in the design.

```html
<!DOCTYPE html>
<html lang="en">
<head>
<meta charset="utf-8">
<title>PBT Advisory – Business Card</title>
<link rel="stylesheet" href="https://fonts.googleapis.com/css2?family=Bodoni+Moda:wght@500&family=Lato:wght@400&display=swap">
<style>
  :root {
    --stage: #4a4947;
    --card-front: #bababa;
    --card-back: #ffffff;
    --ink: #333333;
    --ink-dark: #2b2b2b;
    --rule: #7a7a7a;
  }
  * { margin: 0; padding: 0; box-sizing: border-box; }
  html, body { width: 1200px; height: 1000px; overflow: hidden; }
  body { background: var(--stage); position: relative; }

  .card {
    position: absolute;
    left: 206px;
    width: 788px;
    height: 450px;
    border-radius: 18px;
  }
  .card--front { top: 39px; background: var(--card-front); }
  .card--back  { top: 512px; background: var(--card-back); }

  .brand {
    position: absolute;
    left: 0; right: 0;
    top: 168px;
    text-align: center;
    color: var(--ink);
    font-family: "Bodoni Moda", "Didot", serif;
    font-weight: 500;
  }
  .brand__name {
    font-size: 56px;
    line-height: 70px;
    letter-spacing: 0.5px;
  }
  .brand__tagline {
    margin-top: 2px;
    font-size: 23px;
    letter-spacing: 2.6px;
    line-height: 28px;
  }
  .brand__tagline .dot { font-size: 18px; position: relative; top: -2px; }

  .person {
    position: absolute;
    left: 159px;
    top: 90px;
    color: var(--ink);
  }
  .person__name {
    font-family: "Bodoni Moda", "Didot", serif;
    font-weight: 500;
    font-size: 32px;
    letter-spacing: 1.4px;
    line-height: 40px;
  }
  .person__title {
    font-family: "Lato", Arial, sans-serif;
    font-size: 21px;
    letter-spacing: 0.3px;
    line-height: 26px;
    margin-top: 2px;
  }

  .contact__rule {
    position: absolute;
    left: 234px;
    top: 189px;
    width: 1.5px;
    height: 161px;
    background: var(--rule);
  }
  .contact {
    position: absolute;
    left: 260px;
    top: 224px;
    list-style: none;
    font-family: "Lato", Arial, sans-serif;
    font-size: 21px;
    color: var(--ink-dark);
  }
  .contact__item {
    display: flex;
    align-items: center;
    height: 33px;
  }
  .contact__icon { width: 16px; height: 16px; margin-right: 17px; flex: none; }
</style>
</head>
<body>
  <section class="card card--front">
    <div class="brand">
      <div class="brand__name">PBT ADVISORY</div>
      <div class="brand__tagline"><span class="dot">•</span>VIRTUAL ASSISTANCE<span class="dot">•</span></div>
    </div>
  </section>

  <section class="card card--back">
    <div class="person">
      <div class="person__name">MELANIE HARTWICK</div>
      <div class="person__title">OWNER / CEO</div>
    </div>

    <div class="contact__rule"></div>
    <ul class="contact">
      <li class="contact__item">
        <svg class="contact__icon" viewBox="0 0 16 16" aria-hidden="true">
          <path d="M3.5 1.5l2.3 2.6-1.3 1.8c.9 2 2.4 3.6 4.6 4.6l1.8-1.3 2.6 2.3-1.4 2.2C6.6 13.5 2.5 9.4 1.3 3z" fill="#2b2b2b"/>
          <path d="M9.5 2.5a4 4 0 0 1 4 4M9.5 5a1.6 1.6 0 0 1 1.5 1.5" stroke="#2b2b2b" stroke-width="1.3" fill="none"/>
        </svg>
        <span>240.395.2817</span>
      </li>
      <li class="contact__item">
        <svg class="contact__icon" viewBox="0 0 16 16" aria-hidden="true">
          <path d="M15 1L1 7l5 2 2 6z" fill="#2b2b2b"/>
        </svg>
        <span>info@pbtadvisory.net</span>
      </li>
      <li class="contact__item">
        <svg class="contact__icon" viewBox="0 0 16 16" aria-hidden="true">
          <g fill="none" stroke="#2b2b2b" stroke-width="1.4">
            <circle cx="8" cy="8" r="6.3"/>
            <ellipse cx="8" cy="8" rx="2.8" ry="6.3"/>
            <path d="M1.7 8h12.6M3 4.5h10M3 11.5h10"/>
          </g>
        </svg>
        <span>www.pbtadvisory.net</span>
      </li>
    </ul>
  </section>
</body>
</html>
```